Tovek - Business Card Design

Design a modern masculine business card for our business

Target Market(s)

Private Market

Industry/Entity Type

Construction

Contact Information for Business Card

Company Name - Name of Person - Address - email address - contact number

Font styles to use
Serif
Sans Serif

Colors
0094D4
00A9DD
6FCCEA
C7EBF8
E9F6FB
00AB8E
00BBA5
67D7C9
C6EFE9
E9F9F6
F0912C
F2A743
F7CA91
FBE8D2
FDF5EE

Requirements
Must have
• Use company logo provided
Nice to have
• Company Logo

```html
<!DOCTYPE html>
<html lang="en">
<head>
<meta charset="utf-8">
<title>Tovek – Business Card</title>
<link rel="stylesheet" href="https://fonts.googleapis.com/css2?family=Poppins:wght@400;600;700&display=swap">
<style>
  :root {
    --stage: #2b2724;
    --card: #1b1b1b;
    --orange: #f26f21;
    --white: #ffffff;
    --text-soft: #e6e6e6;
  }
  * { margin: 0; padding: 0; box-sizing: border-box; }
  html, body {
    width: 1200px; height: 842px; overflow: hidden;
    background: var(--stage);
    font-family: "Poppins", sans-serif;
  }
  .canvas {
    position: relative; width: 1200px; height: 842px;
    display: flex; align-items: center; justify-content: center; gap: 50px;
  }
  .card {
    position: relative; width: 525px; height: 300px;
    background: var(--card);
    box-shadow: 0 10px 30px rgba(0,0,0,.45);
    overflow: hidden;
  }
  /* back side */
  .band { position: absolute; left: 0; right: 0; height: 12px; background: var(--orange); }
  .band--top { top: 0; }
  .band--bottom { bottom: 10px; }
  .contact {
    position: absolute; inset: 0;
    display: flex; flex-direction: column; align-items: center; justify-content: center;
    text-align: center; color: var(--text-soft); text-transform: uppercase;
  }
  .contact__name { color: var(--orange); font-weight: 700; font-size: 21px; letter-spacing: .5px; line-height: 1.1; }
  .contact__role { font-size: 13px; letter-spacing: .6px; }
  .rule { width: 52px; height: 1.5px; background: var(--orange); margin: 9px 0; }
  .contact__phone { font-size: 15px; letter-spacing: .5px; line-height: 1.3; }
  .contact__line { font-size: 12.5px; letter-spacing: .4px; line-height: 1.35; }
  .contact__address { margin-top: 14px; }
  /* front side */
  .edge-bar {
    position: absolute; top: 50%; width: 10px; height: 64px;
    transform: translateY(-50%); background: var(--orange);
  }
  .edge-bar--left { left: 0; }
  .edge-bar--right { right: 0; }
  .brand {
    position: absolute; inset: 0;
    display: flex; align-items: center; justify-content: center; gap: 14px;
  }
  .brand__square { width: 18px; height: 18px; background: var(--orange); }
  .brand__name { color: var(--white); font-weight: 700; font-size: 64px; letter-spacing: 4px; text-transform: uppercase; line-height: 1; }
</style>
</head>
<body>
<main class="canvas">
  <section class="card card--back" aria-label="Card back with contact details">
    <div class="band band--top"></div>
    <div class="band band--bottom"></div>
    <div class="contact">
      <p class="contact__name">Marcus Hale</p>
      <p class="contact__role">Managing Director</p>
      <div class="rule"></div>
      <p class="contact__phone">044-210 987 654</p>
      <p class="contact__line">info@tovekbuild.com</p>
      <p class="contact__line">www.tovekbuild.com</p>
      <div class="rule"></div>
      <p class="contact__line contact__address">421, Address Line Goes Here</p>
      <p class="contact__line">45452, Country Name</p>
    </div>
  </section>

  <section class="card card--front" aria-label="Card front with company name">
    <div class="edge-bar edge-bar--left"></div>
    <div class="brand">
      <span class="brand__square"></span>
      <span class="brand__name">Tovek</span>
    </div>
    <div class="edge-bar edge-bar--right"></div>
  </section>
</main>
</body>
</html>
```